Business Card Design Project

We require business cards for "Venoth". We are composed of elite prior military personnel. Our goal is to provide site security for premium businesses who want on the most professional of agents on their premises. Additionally, we will provide executive protection for individuals who require professionalism, flexibility, and dedication

We want this business card to communicate professionalism, dependability, strength. However, we are not an overtly tactical agency and do not want to intimidate our clients personnel or their client. We want to give them a sense of security.
Updates

At the request of one of the designers I've listed the appropriate text that should appear on the card. Please feel free to arrange it in a creative and professional manor.

I've also uploaded a .png file of the triangle logo with no text. Please feel free to incorporate this into your designs.

ThanksĀ 

Target Market(s)

Premium businesses, executives, celebrities, and governments.

Industry/Entity Type

Security

Requirements
Must have
• Text Info that will go on the card. It does not have to be in this order:
Name
Title
Office Phone Number
Cell Phone Number
Email
Website
Mailing Address
Nice to have
• On the back I'd like to see the triangle portion of the logo displayed in a creative way that leaves enough room to write down information if needed.
Should not have
• - Weapons, Globes, or Shields. Every rent-a-cop company has that, and that's not what we are.

```html
<!DOCTYPE html>
<html lang="en">
<head>
<meta charset="utf-8">
<title>Venoth Business Card</title>
<link rel="stylesheet" href="https://fonts.googleapis.com/css2?family=Open+Sans:wght@400;600;700;800&display=swap">
<style>
  :root {
    --bg: #2a2a2c;
    --card: #ffffff;
    --navy: #1d2a44;
    --ink: #2b2b2b;
    --blue: #1e9ad6;
    --blue-deep: #1565b8;
    --blue-light: #4fb3e3;
    --rule: #d9d9d9;
    --ghost: #f0f0f0;
  }
  * { box-sizing: border-box; margin: 0; padding: 0; }
  html, body {
    width: 1200px; height: 926px; overflow: hidden;
    background: var(--bg);
    font-family: "Open Sans", sans-serif;
  }
  .canvas {
    width: 1200px; height: 926px;
    display: flex; align-items: center; justify-content: center; gap: 40px;
  }
  .card {
    position: relative; width: 540px; height: 309px;
    background: var(--card); overflow: hidden;
  }
  /* Front */
  .brand {
    position: absolute; left: 34px; top: 30px;
    display: flex; align-items: center; gap: 10px;
  }
  .brand-mark { width: 22px; height: 22px; background: var(--blue-deep); }
  .brand-name {
    font-weight: 800; font-size: 34px; letter-spacing: 1px;
    color: var(--navy); line-height: 1;
  }
  .person { position: absolute; left: 34px; top: 92px; }
  .person-name { font-size: 26px; color: var(--ink); line-height: 1; }
  .person-name .first { font-weight: 700; }
  .person-name .last { font-weight: 400; }
  .person-title { font-size: 13px; color: var(--blue); margin-top: 3px; }
  .contact { position: absolute; left: 34px; top: 154px; list-style: none; }
  .contact li {
    display: flex; align-items: center; gap: 9px;
    font-size: 11.5px; font-weight: 600; color: var(--ink);
    height: 19px;
  }
  .contact svg { width: 12px; height: 12px; fill: var(--blue); flex: none; }
  .band {
    position: absolute; left: 0; right: 0; bottom: 0; height: 30px;
    background: linear-gradient(to bottom, var(--blue-light) 0 8px, var(--blue) 8px);
  }
  .front-accent {
    position: absolute; right: -40px; bottom: 30px; width: 150px; height: 150px;
    border-radius: 50%;
    background: linear-gradient(135deg, var(--blue-light), var(--blue-deep));
  }
  /* Back */
  .card.back { border: 10px solid var(--blue); }
  .back-mark {
    position: absolute; left: 50%; top: 26px; width: 96px; height: 96px;
    margin-left: -48px; border-radius: 50%;
    background: linear-gradient(135deg, var(--blue-light), var(--blue-deep));
  }
  .ghost-name {
    position: absolute; left: 0; right: 0; top: 132px; text-align: center;
    font-weight: 800; font-size: 72px; letter-spacing: 4px; color: var(--ghost);
    line-height: 1;
  }
  .write-lines { position: absolute; left: 0; right: 0; top: 222px; }
  .write-lines span { display: block; height: 1px; background: var(--rule); margin-bottom: 26px; }
</style>
</head>
<body>
<main class="canvas">
  <section class="card front" aria-label="Card front">
    <div class="brand">
      <span class="brand-mark"></span>
      <span class="brand-name">VENOTH</span>
    </div>
    <div class="person">
      <p class="person-name"><span class="first">MARCUS</span> <span class="last">HALE</span></p>
      <p class="person-title">Graphic Designer</p>
    </div>
    <ul class="contact">
      <li><svg viewBox="0 0 12 12"><path d="M6 0a4 4 0 0 0-4 4c0 3 4 8 4 8s4-5 4-8a4 4 0 0 0-4-4zm0 5.6A1.6 1.6 0 1 1 6 2.4a1.6 1.6 0 0 1 0 3.2z"/></svg>78 Harbor Ridge Rd, Westfall NY 10482</li>
      <li><svg viewBox="0 0 12 12"><circle cx="6" cy="6" r="6"/></svg>www.venoth.com</li>
      <li><svg viewBox="0 0 12 12"><path d="M1 4c0-2 2-3 5-3s5 1 5 3H8.5V3h-5v1zM2 5h8l1 6H1z"/></svg>+1 (212) 555-0147</li>
      <li><svg viewBox="0 0 12 12"><path d="M2.5 0.5l2 2-1 1.5c.7 1.6 2 2.9 3.5 3.5L8.5 6.5l2 2-1.5 2C5 10 2 7 1 2z"/></svg>+1 (917) 555-0183</li>
      <li><svg viewBox="0 0 12 12"><path d="M0 2h12v8H0zm1 1v.3l5 3.2 5-3.2V3zm0 1.5V9h10V4.5L6 7.7z"/></svg>mhale@venoth.com</li>
    </ul>
    <div class="front-accent"></div>
    <div class="band"></div>
  </section>

  <section class="card back" aria-label="Card back">
    <div class="back-mark"></div>
    <p class="ghost-name">VENOTH</p>
    <div class="write-lines"><span></span><span></span></div>
  </section>
</main>
</body>
</html>
```